Medical program Ombo produce by VALORENZA

I need a business card of the program to give to the customer to get the general information to contact the clinic. I need a bilingual card French and English you will see the logo.
That's a program that the Clinic Valorenza offers. https://medicalombo.ca
Program: Ombo Medical Program
Slogan: Lose weight - Breathe - Live / Be light - Breathe - Live
The clinic that offers the program: Valorenza
Website: https://medicalombo.ca
---
Medical team / Medical team
email: doc@valorenza.ca
phone: 514 555-0147
Information
email: ombo@valorenza.ca
phone: 514 555-0183 ext 3
Target Market(s)
Every person that needs to lose weight
Industry/Entity Type
Health clinic for obese person
Contact Information for Business Card
All the information in the description
Requirements
Must have
- Look clean - Expensive clinic / Need to be bilingual
Nice to have
- Recto verso for french and english
Should not have
- -

```html
<!DOCTYPE html>
<html lang="en">
<head>
<meta charset="utf-8">
<title>Ombo Medical Program – Business Card</title>
<link rel="stylesheet" href="https://fonts.googleapis.com/css2?family=Source+Sans+3:wght@400;600&display=swap">
<style>
  :root {
    --backdrop: #e9e9e7;
    --card: #ffffff;
    --teal: #00a396;
    --blue: #1b7fcf;
    --ink: #111111;
    --white: #ffffff;
  }
  * { box-sizing: border-box; margin: 0; padding: 0; }
  html, body {
    width: 1200px;
    height: 857px;
    overflow: hidden;
    background: var(--backdrop);
    font-family: "Source Sans 3", "Myriad Pro", Arial, sans-serif;
  }
  .card {
    position: absolute;
    left: 75px;
    top: 128px;
    width: 1050px;
    height: 600px;
    background: var(--card);
    overflow: hidden;
    box-shadow: 0 6px 24px rgba(0,0,0,0.12);
  }
  .side-band {
    position: absolute;
    right: 0;
    top: 0;
    width: 300px;
    height: 600px;
  }
  .brand {
    position: absolute;
    left: 150px;
    top: 60px;
    width: 560px;
  }
  .brand-name {
    display: flex;
    align-items: center;
    gap: 18px;
    color: var(--teal);
    font-weight: 400;
    font-size: 130px;
    line-height: 1;
    letter-spacing: 2px;
  }
  .brand-dot {
    width: 26px;
    height: 26px;
    border-radius: 50%;
    background: var(--teal);
  }
  .slogan {
    margin-top: 10px;
    color: var(--blue);
    font-size: 24px;
    white-space: nowrap;
  }
  .program {
    position: absolute;
    left: 90px;
    top: 290px;
    width: 620px;
    text-align: center;
  }
  .program-name {
    color: var(--ink);
    font-size: 50px;
    font-weight: 400;
    line-height: 1.05;
    white-space: nowrap;
  }
  .program-url {
    color: var(--blue);
    font-size: 36px;
    line-height: 1.2;
    white-space: nowrap;
  }
  .contact {
    position: absolute;
    font-size: 28px;
    line-height: 1.3;
    color: var(--ink);
    white-space: nowrap;
  }
  .contact-title { color: var(--blue); }
  .contact-row { display: flex; align-items: center; gap: 12px; }
  .contact--team { left: 90px; top: 455px; }
  .contact--info { right: 310px; top: 415px; text-align: right; }
  .contact--info .contact-row { justify-content: flex-end; }
  .icon { width: 22px; height: 22px; flex: none; }
</style>
</head>
<body>
  <main class="card">
    <svg class="side-band" viewBox="0 0 300 600" role="img" aria-label="Teal side band">
      <path d="M120 0 C20 160 30 300 80 420 C110 500 100 560 90 600 L300 600 L300 0 Z" fill="var(--teal)"/>
    </svg>

    <header class="brand">
      <div class="brand-name"><span class="brand-dot"></span>Ombo</div>
      <p class="slogan">Lose weight - Breathe - Live / Be light - Breathe - Live</p>
    </header>

    <section class="program">
      <h1 class="program-name">Ombo Medical Program</h1>
      <p class="program-url">www.medicalombo.ca</p>
    </section>

    <section class="contact contact--team">
      <p class="contact-title">Medical team / Medical team</p>
      <p class="contact-row">
        <svg class="icon" viewBox="0 0 22 22"><rect width="22" height="22" fill="var(--teal)"/><rect x="4" y="6" width="14" height="10" fill="none" stroke="var(--white)" stroke-width="1.6"/><path d="M4 6 L11 12 L18 6" fill="none" stroke="var(--white)" stroke-width="1.6"/></svg>
        doc@valorenza.ca
      </p>
      <p class="contact-row">
        <svg class="icon" viewBox="0 0 22 22"><rect width="22" height="22" fill="var(--teal)"/><path d="M7 4 L10 8 L8.5 10 C9.5 12 10.5 13 12 13.5 L14 12 L18 15 L16 18 C10 18 5 12 5 6 Z" fill="var(--white)"/></svg>
        514 555-0147
      </p>
    </section>

    <section class="contact contact--info">
      <p class="contact-title">Information</p>
      <p class="contact-row">
        ombo@valorenza.ca
        <svg class="icon" viewBox="0 0 22 22"><rect width="22" height="22" fill="var(--teal)"/><rect x="4" y="6" width="14" height="10" fill="none" stroke="var(--white)" stroke-width="1.6"/><path d="M4 6 L11 12 L18 6" fill="none" stroke="var(--white)" stroke-width="1.6"/></svg>
      </p>
      <p class="contact-row">
        514 555-0183 ext 3
        <svg class="icon" viewBox="0 0 22 22"><rect width="22" height="22" fill="var(--teal)"/><path d="M7 4 L10 8 L8.5 10 C9.5 12 10.5 13 12 13.5 L14 12 L18 15 L16 18 C10 18 5 12 5 6 Z" fill="var(--white)"/></svg>
      </p>
    </section>
  </main>
</body>
</html>
```